Vintage themed home decor Shopify store needs sales promotion banner ads

"Quill & Lantern Goods" is an Australian based lifestyle home decor store that sells vintage, retro and antique relic replicas and reproduction items online to their local customers Australia wide.

We need banner ads for our store home page slider that promotes our unique products, new stock arrival and calls store visitors to to buy from our different product collections.

We anticipate that we will need multiple banner ads, primarily for the following product collections:
1. Sundials & Compass
2. Airplane models
3. Magnifying glass
4. Clocks & Watches

Banners could also be generic with generic discount coupon promotions.

Banners should be based around the theme of our store and products which gives a sense of colonial / vintage lifestyle and that they compliment the colour & theme of the store.

Banner Size: 1600 x 800 px

Please find attached some samples of the types of banner ads we have in mind and also our logo. Product images can be supplied if they are required to be used in the ads.

Website URL: https://quillandlanterngoods.example

Target Market(s)

mostly Males aged between 35-65.
Products ideally for man-cave & office decor.

Industry/Entity Type

Home And Garden

Font styles to use
Serif
Decorative
Script

Requirements
Must have
• some product images
Nice to have
• lifestyle shots.
• blank space to insert for a coupon code
Should not have
• caricatures & cartoon

```html
<!DOCTYPE html>
<html lang="en">
<head>
<meta charset="utf-8">
<title>Sundials &amp; Compass — Quill &amp; Lantern Goods</title>
<link rel="stylesheet" href="https://fonts.googleapis.com/css2?family=Playball&family=Crete+Round&display=swap">
<style>
  :root {
    --sea-light: #9cc3dc;
    --sea-mid: #7fabc9;
    --sea-deep: #6a98b8;
    --band: #55707e;
    --band-line: #c9dbe6;
    --frame-line: rgba(235, 243, 248, 0.7);
    --card-paper: #e9eff2;
    --card-paper-edge: #c7d4db;
    --wood: #7a3f22;
    --brass: #8a6a3a;
    --ink: #2e3a40;
    --seal-rim: #1f1f1f;
    --seal-line: #d8cfb8;
    --seal-face: #dfe8ed;
  }
  * { margin: 0; padding: 0; box-sizing: border-box; }
  html, body { width: 1200px; height: 600px; overflow: hidden; background: #fff; }
  .banner { position: relative; width: 1200px; height: 600px; overflow: hidden; }
  .banner__sea {
    position: absolute; inset: 0;
    background: linear-gradient(170deg, var(--sea-light) 0%, var(--sea-mid) 55%, var(--sea-deep) 100%);
  }
  .banner__frame { position: absolute; inset: 11px; border: 1.5px solid var(--frame-line); }
  .banner__band {
    position: absolute; left: 0; right: 0; top: 410px; height: 88px;
    background: var(--band);
    border-top: 2px solid var(--band-line);
    border-bottom: 2px solid var(--band-line);
  }
  .product-card {
    position: absolute;
    background: radial-gradient(ellipse at center, var(--card-paper) 40%, var(--card-paper-edge) 100%);
    box-shadow: 0 2px 8px rgba(0,0,0,0.15);
  }
  .product-card--boxed { left: 45px; top: 78px; width: 405px; height: 380px; }
  .product-card--open { left: 430px; top: 287px; width: 322px; height: 266px; }
  .product-card__photo { position: absolute; border-radius: 6px; }
  .product-card--boxed .product-card__photo {
    left: 72px; top: 18px; width: 278px; height: 330px;
    background: linear-gradient(160deg, #5e2c16 0%, var(--wood) 40%, var(--brass) 65%, var(--wood) 100%);
  }
  .product-card--open .product-card__photo {
    left: 40px; top: 18px; width: 245px; height: 220px; border-radius: 50%;
    background: radial-gradient(circle at 50% 45%, #a98650 0%, var(--brass) 45%, #4a2a18 100%);
  }
  .headline {
    position: absolute; left: 535px; top: 40px; width: 600px; text-align: center; color: var(--ink);
  }
  .headline__rule { display: block; margin: 0 auto; }
  .headline__title {
    font-family: "Playball", cursive; font-weight: 400; font-size: 72px; line-height: 1;
    margin-top: 16px;
  }
  .headline__tagline {
    font-family: "Crete Round", serif; font-weight: 400; font-size: 34px; line-height: 1.12;
    margin: 12px 0 18px;
  }
  .shop-seal { position: absolute; left: 942px; top: 352px; width: 206px; height: 206px; display: block; }
</style>
</head>
<body>
<main class="banner">
  <div class="banner__sea" role="img" aria-label="Calm blue sea water surface"></div>
  <div class="banner__band"></div>
  <div class="banner__frame"></div>

  <figure class="product-card product-card--boxed">
    <div class="product-card__photo" role="img" aria-label="Brass sundial compass resting in an open wooden presentation box"></div>
  </figure>
  <figure class="product-card product-card--open">
    <div class="product-card__photo" role="img" aria-label="Antique brass sundial compass with raised gnomon and spirit level"></div>
  </figure>

  <header class="headline">
    <svg class="headline__rule" width="340" height="6" viewBox="0 0 340 6" aria-hidden="true">
      <line x1="0" y1="3" x2="340" y2="3" stroke="var(--ink)" stroke-width="2"/>
    </svg>
    <h1 class="headline__title">Sundials &amp; Compass</h1>
    <p class="headline__tagline">Get your bearings straight<br>with these beautiful replicas</p>
    <svg class="headline__rule" width="340" height="6" viewBox="0 0 340 6" aria-hidden="true">
      <line x1="0" y1="3" x2="340" y2="3" stroke="var(--ink)" stroke-width="2"/>
    </svg>
  </header>

  <a class="shop-seal" href="https://quillandlanterngoods.example" aria-label="Shop now">
    <svg width="206" height="206" viewBox="0 0 206 206" aria-hidden="true">
      <circle cx="103" cy="103" r="101" fill="var(--seal-rim)"/>
      <circle cx="103" cy="103" r="68" fill="var(--seal-face)" stroke="var(--seal-line)" stroke-width="2"/>
    </svg>
  </a>
</main>
</body>
</html>
```